Somebody commencing retirement at age 67 and wanting a card to introduce myself

Something that depicts the activities I intend to pursue in retirement: Travel, Golf (both in Australia and internationally), wining (red) and dining and generally leading a decadent lifestyle with my wife (or by myself as appropriate).

I offer no services, but intend to have a decadent, relaxing
retirement, playing golf, drinking red wine and dining at good
restaurants!

The card needs to have a suitably designed logo that reflects the
foregoing.

Requirements
Must have
• On the front of the card, my photograph (attached and cropped as
• appropriate), my name (Neil Corbishley), my mobile phone number (+61 417
• 382 514), my email address (neil@corbishley.net.au) and my residential
• address (41 Marlowvale Road, Kestrelton, Western Australia 6187,
• Australia).
• The rear of the card should have my postal address (Neil Corbishley
• Post Office Box 418 Brindlecove Western Australia 6951, Australia.)._

```html
<!DOCTYPE html>
<html lang="en">
<head>
<meta charset="utf-8">
<title>Neil Corbishley – Business Card</title>
<link href="https://fonts.googleapis.com/css2?family=Lato:wght@300;400;700&display=swap" rel="stylesheet">
<style>
  :root {
    --canvas-bg: #e4e4e4;
    --card-dark: #3d3d3d;
    --card-dark-edge: #333333;
    --card-light: #ffffff;
    --ink-light: #ffffff;
    --ink-dark: #3a3a3a;
    --ink-muted: #6b6b6b;
    --rule: #8a8a8a;
  }
  * { margin: 0; padding: 0; box-sizing: border-box; }
  html, body {
    width: 1200px;
    height: 930px;
    overflow: hidden;
    background: var(--canvas-bg);
    font-family: "Lato", sans-serif;
  }
  .canvas {
    position: relative;
    width: 1200px;
    height: 930px;
  }
  .card {
    position: absolute;
    left: 290px;
    width: 620px;
    height: 360px;
    border-radius: 26px;
    box-shadow: 0 6px 18px rgba(0,0,0,0.18);
  }

  /* Back of card */
  .card--back {
    top: 60px;
    background: linear-gradient(120deg, var(--card-dark-edge) 0%, var(--card-dark) 45%, #4a4a4a 55%, var(--card-dark) 100%);
    color: var(--ink-light);
  }
  .brand {
    position: absolute;
    left: 150px;
    top: 100px;
    display: flex;
    align-items: center;
    gap: 22px;
  }
  .brand__circle {
    width: 110px;
    height: 110px;
    border: 2px solid var(--ink-light);
    border-radius: 50%;
  }
  .brand__name {
    font-weight: 300;
    font-size: 26px;
    letter-spacing: 3px;
    text-transform: uppercase;
  }
  .postal-address {
    position: absolute;
    left: 0;
    right: 0;
    bottom: 48px;
    text-align: center;
    font-size: 15px;
    font-weight: 400;
    letter-spacing: 0.3px;
  }

  /* Front of card */
  .card--front {
    top: 500px;
    background: var(--card-light);
  }
  .identity {
    position: absolute;
    top: 118px;
    left: 0;
    right: 0;
    display: flex;
    justify-content: center;
    align-items: center;
    gap: 26px;
  }
  .identity__who { text-align: right; }
  .identity__name {
    font-weight: 700;
    font-size: 19px;
    color: var(--ink-dark);
    text-transform: uppercase;
    letter-spacing: 0.4px;
  }
  .identity__role {
    font-size: 14px;
    color: var(--ink-muted);
    margin-top: 2px;
  }
  .identity__rule {
    width: 1px;
    height: 46px;
    background: var(--rule);
  }
  .contacts {
    list-style: none;
    font-size: 14px;
    color: var(--ink-dark);
    line-height: 1.6;
  }
  .contacts li { display: flex; align-items: center; gap: 8px; }
  .contacts svg { width: 12px; height: 12px; flex: none; }
  .residential-address {
    position: absolute;
    left: 0;
    right: 0;
    bottom: 52px;
    text-align: center;
    font-size: 15px;
    color: var(--ink-muted);
  }
</style>
</head>
<body>
<main class="canvas">
  <section class="card card--back" aria-label="Back of card">
    <div class="brand">
      <span class="brand__circle" aria-hidden="true"></span>
      <span class="brand__name">Neil Corbishley</span>
    </div>
    <p class="postal-address">Box 418 Brindlecove Western Australia 6951, Australia.</p>
  </section>

  <section class="card card--front" aria-label="Front of card">
    <div class="identity">
      <div class="identity__who">
        <p class="identity__name">Neil Corbishley</p>
        <p class="identity__role">Photograph</p>
      </div>
      <span class="identity__rule" aria-hidden="true"></span>
      <ul class="contacts">
        <li>
          <svg viewBox="0 0 12 12" aria-hidden="true"><path d="M2.5 1 L4.5 1 L5.2 3.4 L4 4.3 C4.6 5.8 6.2 7.4 7.7 8 L8.6 6.8 L11 7.5 L11 9.5 C11 10.3 10.3 11 9.5 11 C5 11 1 7 1 2.5 C1 1.7 1.7 1 2.5 1 Z" fill="none" stroke="#3a3a3a" stroke-width="1"/></svg>
          (+61 417 - 382 514)
        </li>
        <li>
          <svg viewBox="0 0 12 12" aria-hidden="true"><rect x="1" y="2.5" width="10" height="7" fill="none" stroke="#3a3a3a" stroke-width="1"/><path d="M1 2.5 L6 6.5 L11 2.5" fill="none" stroke="#3a3a3a" stroke-width="1"/></svg>
          neil@corbishley.net.au
        </li>
      </ul>
    </div>
    <p class="residential-address">41 Marlowvale Road, Kestrelton, Western Australia 6187, Australia</p>
  </section>
</main>
</body>
</html>
```